Nobre Lente Lusitana - business card

Create a business card for my eyewear (glasses) store. The concept is based in handcrafted glasses (as well as common frames and 3d printed), clean, and elegant. The business card could be black (white letters and symbols) or white (black letters and symbols) but we are open to new suggestions. It must be sober and elegant.
The name Nobre Lente Lusitana means Royal/Real Portuguese Optical Store.
Our concept should be inspired by the pictures attatched bellow.
I would like it to be classic and elegant as business cards for bankers.
Our first selected logo is also available in attachment files.

Target Market(s)

For business meetings with investors, supliers and fairs

Industry/Entity Type

Eyewear

Contact Information for Business Card

Some random business cards in attachment that we like. Don't be closed to it, we like freedom of think.

Font styles to use
Serif
Sans Serif

Colors
404040
e9e9e9
fbfbfb
000000
85abd3
0255a3
f7fbfd
959595

Requirements
Must have
• Must be elegant, simple.
• Must present our brand new logo (slight variations are welcome, the logo is not closed yet). See our temporary logo in attachment.
• Black (or dark grey), white (or light grey) and a third slight color.
• This third slight color could be dark blue or grayish blue.
• Info:
• Fernando Amaral (name)
• famaral@nobrelentelusitana.example
• +351 936204518
• www.nobrelentelusitana.example
Nice to have
• Black and white or with serious colors such as dark blue or greyish blue.
• Could also have water mark with our logo (big size) in the background (inspired in KVN bank credit card design)
Should not have
• Hysteric colora or shapes

```html
<!DOCTYPE html>
<html lang="pt">
<head>
<meta charset="utf-8">
<title>Nobre Lente Lusitana – business card</title>
<link rel="stylesheet" href="https://fonts.googleapis.com/css2?family=Open+Sans:wght@300;400;600&display=swap">
<style>
  :root {
    --backdrop: #e9e9e9;
    --card-light: #fbfbfb;
    --card-dark: #111111;
    --ink-dark: #000000;
    --ink-light: #f2f2f2;
    --ink-muted: #cfcfcf;
    --rule: #8a8a8a;
  }
  * { box-sizing: border-box; margin: 0; padding: 0; }
  html, body {
    width: 1200px; height: 900px; overflow: hidden;
    background: var(--backdrop);
    font-family: "Open Sans", Arial, sans-serif;
  }
  .canvas {
    width: 1200px; height: 900px;
    display: flex; align-items: center; justify-content: center; gap: 60px;
  }
  .card {
    width: 510px; height: 300px;
    position: relative;
    box-shadow: 0 10px 28px rgba(0,0,0,.18);
  }
  .card--front {
    background: var(--card-light);
    display: flex; flex-direction: column; align-items: center; justify-content: center;
    gap: 16px;
  }
  .brand-mark {
    width: 14px; height: 14px; border-radius: 50%;
    border: 2px solid var(--ink-dark);
  }
  .brand-name {
    font-weight: 600; font-size: 19px; letter-spacing: .06em;
    text-transform: uppercase; color: var(--ink-dark);
  }
  .card--back {
    background: var(--card-dark);
    color: var(--ink-light);
    padding: 54px 0 0 64px;
  }
  .person-name {
    font-weight: 400; font-size: 25px; letter-spacing: .2em;
    text-transform: uppercase;
  }
  .dividers { position: relative; height: 46px; margin-top: 12px; }
  .divider { position: absolute; height: 1px; width: 100px; background: var(--rule); }
  .divider--upper { left: 210px; top: 8px; }
  .divider--lower { left: 150px; top: 34px; }
  .contact { list-style: none; margin-top: 14px; }
  .contact li {
    font-weight: 300; font-size: 14px; line-height: 1.55;
    color: var(--ink-muted); letter-spacing: .02em;
  }
</style>
</head>
<body>
  <main class="canvas">
    <section class="card card--front" aria-label="Card front">
      <span class="brand-mark" aria-hidden="true"></span>
      <h1 class="brand-name">Nobre Lente Lusitana</h1>
    </section>
    <section class="card card--back" aria-label="Card back">
      <h2 class="person-name">Fernando Amaral</h2>
      <div class="dividers" aria-hidden="true">
        <span class="divider divider--upper"></span>
        <span class="divider divider--lower"></span>
      </div>
      <ul class="contact">
        <li>+351 936204518</li>
        <li>www.nobrelentelusitana.example</li>
        <li>famaral@nobrelentelusitana.example</li>
      </ul>
    </section>
  </main>
</body>
</html>
```